Sunvale Hearth Roti/Naan bread packaging for Australia

We would like to update and refresh the packaging design for our Sunvale Hearth bread range. These breads are currently being sold in Australian supermarkets and are very popular. The proposed design should have some "continuity" with the current packaging design so that consumers can still recognise the brand/product easily on shelf. The design should suggest "fresh, tasty, healthy, authentic and Australian-made".
FYI, the products are not chilled or frozen - they sit on the regular supermarket shelves and will need to stand out. The breads will typically sit next to each other on the shelf, but usually just one facing each. I'll be uploading image files of the current packaging for your reference.
Updates

Hi all, I just uploaded the current logo for those of you who want it.  Also, there are printer details in the discussion area that you might find useful.  I am hoping to get their design template in the next day or so, but don't let that stop you from starting.  We are only looking for a design concept that we can use across the product range.  Cheers!

Hi, I've uploaded the design template/layers for those who would like this.  Cheers!

Hi everyone, thanks to those of you who have either submitted or are working on designs.  I have reviewed the available designs with the MD and will be providing individual feedback to you wherever possible.

Lastly, we'll be extending the deadline for a few more days to allow for changes and resubmissions.

Good luck everyone!

Reason: To allow for changes and resubmissions - will be providing individual feedback to all designs submitted. Cheers.

Reason: One last extension before we award the guaranteed prize.

Target Market(s)

Australian consumers who eat Indian foods and would pay a premium for a better product

Industry/Entity Type

Product

Requirements
Must have
• Transparent window to show breads
Some carryover elements from current packaging for consumer recognition
Same product info on the back (i.e. Nutritional Info panel, Heating Instructions, Barcode, Company details, Usage Suggestions)
Nice to have
• The design should suggest "fresh, tasty, healthy, authentic and Australian-made".

```html
<!DOCTYPE html>
<html lang="en">
<head>
<meta charset="utf-8">
<title>Sunvale Hearth Roti Bread – Garlic Flavour</title>
<link href="https://fonts.googleapis.com/css2?family=Kalam:wght@400;700&display=swap" rel="stylesheet">
<style>
  :root {
    --pack-top: #f5561e;
    --pack-mid: #e8381a;
    --pack-bottom: #c50f0e;
    --field-tone: #d8301a;
    --pattern-tone: rgba(180, 30, 10, 0.18);
    --brand-yellow: #ffe83a;
    --white: #ffffff;
    --ink: #1c1110;
    --badge-dark: #2a0e08;
    --badge-edge: #130503;
    --slot-edge: #b9b9b9;
    --veg-green: #2dcc2d;
    --seal-line: #d9c7c2;
  }

  html, body {
    margin: 0;
    padding: 0;
    overflow: hidden;
    background: #ffffff;
  }

  .pack {
    position: relative;
    width: 950px;
    height: 1200px;
    overflow: hidden;
    background: linear-gradient(180deg, var(--pack-top) 0%, var(--pack-top) 22%, var(--pack-mid) 50%, var(--pack-bottom) 100%);
    font-family: "Kalam", cursive;
  }

  .floral-pattern {
    position: absolute;
    left: 0;
    top: 270px;
    width: 950px;
    height: 700px;
    background: radial-gradient(ellipse at 50% 50%, var(--pattern-tone) 0%, rgba(0,0,0,0) 70%);
  }

  .wheat-field {
    position: absolute;
    left: 0;
    top: 810px;
    width: 950px;
    height: 290px;
    background: linear-gradient(180deg, rgba(216,48,26,0) 0%, var(--field-tone) 55%, rgba(197,15,14,0) 100%);
  }

  .hang-slot {
    position: absolute;
    left: 371px;
    top: 69px;
    width: 207px;
    height: 40px;
    border-radius: 20px;
    background: var(--white);
    box-shadow: inset 0 -2px 0 var(--slot-edge);
  }

  .brand-name {
    position: absolute;
    left: 0;
    top: 205px;
    width: 938px;
    margin: 0;
    text-align: center;
    font-family: "Kalam", cursive;
    font-weight: 700;
    font-size: 66px;
    line-height: 1;
    color: var(--brand-yellow);
  }

  .claim-badge {
    position: absolute;
    left: 38px;
    top: 274px;
    width: 222px;
    height: 222px;
  }

  .claim-badge__text {
    position: absolute;
    left: 38px;
    top: 352px;
    width: 222px;
    text-align: center;
    font-size: 23px;
    line-height: 29px;
    color: var(--brand-yellow);
  }

  .badge-pin {
    position: absolute;
    left: 138px;
    top: 272px;
    width: 40px;
    height: 40px;
    border-radius: 50%;
    background: radial-gradient(circle at 40% 35%, #ffe46a 0%, #f1b10c 60%, #b77a00 100%);
  }

  .product-name {
    position: absolute;
    left: 284px;
    top: 372px;
    margin: 0;
    font-size: 70px;
    font-weight: 400;
    line-height: 1;
    color: var(--white);
    text-shadow: 3px 3px 0 var(--ink);
    white-space: nowrap;
  }

  .origin {
    position: absolute;
    left: 297px;
    top: 458px;
    margin: 0;
    font-size: 25px;
    line-height: 1;
    color: var(--ink);
  }

  .window {
    position: absolute;
    left: 0;
    top: 0;
    width: 950px;
    height: 1200px;
  }

  .flavour {
    position: absolute;
    left: 0;
    top: 862px;
    width: 956px;
    text-align: center;
    margin: 0;
    font-size: 34px;
    line-height: 1;
    color: var(--ink);
  }

  .net-weight {
    position: absolute;
    left: 40px;
    top: 1058px;
    display: flex;
    align-items: center;
    gap: 8px;
    font-family: Arial, Helvetica, sans-serif;
    font-size: 17px;
    color: var(--ink);
  }

  .veg-mark {
    width: 13px;
    height: 13px;
    border: 2px solid var(--white);
    background: var(--veg-green);
    box-sizing: content-box;
  }

  .halal-seal {
    position: absolute;
    left: 834px;
    top: 1014px;
    width: 84px;
    height: 84px;
  }
</style>
</head>
<body>
<main class="pack">
  <div class="floral-pattern" role="img" aria-label="Faint floral scroll pattern across the pack"></div>
  <div class="wheat-field" role="img" aria-label="Silhouette of a wheat field along the lower pack"></div>

  <div class="hang-slot"></div>

  <p class="brand-name">Sunvale Hearth</p>

  <svg class="claim-badge" viewBox="0 0 222 222" aria-hidden="true">
    <polygon fill="var(--badge-edge)" transform="translate(5 6)"
      points="111,2 124,22 144,7 150,31 174,23 171,48 196,48 185,71 209,80 191,98 211,113 189,127 204,148 179,154 188,178 163,176 162,201 139,191 130,215 111,199 92,215 83,191 60,201 59,176 34,178 43,154 18,148 33,127 11,113 31,98 13,80 37,71 26,48 51,48 48,23 72,31 78,7 98,22"/>
    <polygon fill="var(--badge-dark)"
      points="111,2 124,22 144,7 150,31 174,23 171,48 196,48 185,71 209,80 191,98 211,113 189,127 204,148 179,154 188,178 163,176 162,201 139,191 130,215 111,199 92,215 83,191 60,201 59,176 34,178 43,154 18,148 33,127 11,113 31,98 13,80 37,71 26,48 51,48 48,23 72,31 78,7 98,22"/>
  </svg>
  <div class="badge-pin" role="img" aria-label="Yellow push pin holding the badge"></div>
  <div class="claim-badge__text">Fresh &amp; Pure<br>Healthy<br>Tasty</div>

  <h1 class="product-name">Roti Bread</h1>
  <p class="origin">Australian Made</p>

  <svg class="window" viewBox="0 0 950 1200" aria-hidden="true">
    <polygon fill="var(--white)" points="188,500 370,592 318,628"/>
    <ellipse fill="var(--white)" cx="505" cy="760" rx="284" ry="246"/>
  </svg>

  <p class="flavour">Garlic Flavour</p>

  <div class="net-weight"><span class="veg-mark"></span><span>280 gm. NET</span></div>

  <svg class="halal-seal" viewBox="0 0 84 84" aria-label="Certification seal" role="img">
    <circle cx="42" cy="42" r="39" fill="none" stroke="var(--seal-line)" stroke-width="2"/>
  </svg>
</main>
</body>
</html>
```